Flyer für Handwerksunternehmen
Zielgruppe
Wir sind ein Handwerksunternehmen. Wir bieten alle Leistungen aus einer Hand. Mehr Infos unter www.werkbaukolleg.de
Aufgabenstellung
Modernes Design

```html
<!DOCTYPE html>
<html lang="de">
<head>
<meta charset="utf-8">
<title>werkbaukolleg – Flyer</title>
<link href="https://fonts.googleapis.com/css2?family=Poppins:wght@300;400;700&family=Roboto+Condensed:wght@400;500&family=Barlow+Semi+Condensed:wght@400;500&display=swap" rel="stylesheet">
<style>
  :root{
    --stage:#1c1c1c;
    --green-dark:#1d6a2f;
    --green:#6a9f3a;
    --green-light:#8dbb4c;
    --paper:#ffffff;
    --ink:#2b2b2b;
    --ink-soft:#4a4a4a;
  }
  *{margin:0;padding:0;box-sizing:border-box}
  html,body{width:1200px;height:808px;overflow:hidden;background:var(--stage)}
  .stage{position:relative;width:1200px;height:808px}
  .panel{position:absolute;top:123px;width:562px;height:562px;overflow:hidden}
  .panel--front{left:38px;background:var(--paper)}
  .panel--back{left:621px;background:linear-gradient(160deg,#f1f1f1,#e5e5e5)}
  .abs{position:absolute}

  /* front */
  .brand{font-family:'Poppins',sans-serif;font-weight:700;color:var(--green-dark);font-size:17px;display:flex;align-items:center;gap:8px;letter-spacing:.2px}
  .brand__square{width:14px;height:14px;background:var(--green)}
  .front-brand{left:22px;top:70px}
  .headline{left:23px;top:156px;font-family:'Poppins',sans-serif;font-weight:700;color:var(--green-dark);font-size:23px;line-height:25px}
  .subline{left:23px;top:212px;font-family:'Poppins',sans-serif;font-weight:400;color:var(--green);font-size:22.5px;line-height:22px}
  .intro{left:19px;top:269px;width:314px;height:274px}
  .intro__text{position:absolute;left:11px;top:8px;width:290px;font-family:'Roboto Condensed',sans-serif;font-size:11.4px;line-height:14.2px;color:#fff;text-align:justify}
  .intro__notch{float:right;width:30px;height:14px}
  .intro__text b{font-weight:500}
  .building{left:250px;top:12px;width:312px;height:282px}
  .comp-title{left:340px;top:312px;width:208px;text-align:center;font-family:'Poppins',sans-serif}
  .comp-title__light{font-weight:300;font-size:16px;line-height:18px;color:var(--ink-soft)}
  .comp-title__bold{font-weight:700;font-size:17.5px;line-height:22px;color:var(--green)}
  .tile{position:absolute;width:64px;height:80px;display:flex;flex-direction:column;align-items:center;justify-content:flex-end;padding-bottom:11px;font-family:'Roboto Condensed',sans-serif;font-size:7.4px;line-height:10.5px;text-align:center;white-space:nowrap;letter-spacing:-.15px;clip-path:polygon(0 0,calc(100% - 8px) 0,100% 8px,100% 100%,8px 100%,0 calc(100% - 8px))}
  .tile__icon{position:absolute;top:11px;left:50%;width:26px;height:26px;margin-left:-13px;border:1.5px solid currentColor;border-radius:2px;opacity:.8;z-index:1}
  .tile--outline{background:var(--green-dark);color:var(--green-dark)}
  .tile--outline::before{content:"";position:absolute;inset:1.5px;background:#fff;clip-path:inherit}
  .tile--soft{background:var(--green-light);color:var(--green)}
  .tile--soft::before{content:"";position:absolute;inset:1.5px;background:#fff;clip-path:inherit}
  .tile--dark{background:var(--green-dark);color:#fff}
  .tile--mid{background:var(--green);color:#fff}
  .tile span{position:relative}

  /* back */
  .services-head{left:27px;top:19px;font-family:'Poppins',sans-serif;color:#fff}
  .services-head__light{font-weight:300;font-size:18.5px;line-height:22px;letter-spacing:.3px}
  .services-head__bold{font-weight:700;font-size:19.5px;line-height:26px}
  .services{list-style:none;font-family:'Barlow Semi Condensed',sans-serif;font-weight:500;font-size:22.5px;line-height:29.6px;color:var(--green-dark)}
  .services li{position:relative;padding-left:16px}
  .services li::before{content:"";position:absolute;left:0;top:12px;width:6px;height:6px;background:var(--green-light)}
  .services--left{left:27px;top:99px}
  .services--right{left:294px;top:99px}
  .claim{left:36px;top:393px;width:484px;text-align:center;font-family:'Barlow Semi Condensed',sans-serif;font-size:18px;color:var(--ink)}
  .claim b{font-weight:500;color:var(--ink)}
  .back-brand{left:60px;top:474px}
  .contact{font-family:'Poppins',sans-serif;color:var(--ink-soft);font-size:14px;line-height:18px}
  .contact__row{position:absolute;left:0;display:flex;gap:9px;align-items:flex-start;white-space:nowrap}
  .contact__phone{font-weight:700;font-size:21px;color:var(--green-dark);line-height:26px}
  .contact svg{flex:none;margin-top:2px}
</style>
</head>
<body>
<div class="stage">

  <section class="panel panel--front">
    <svg class="abs" style="left:0;top:0" width="562" height="562" aria-hidden="true">
      <polygon points="0,158 219,90 219,95 0,167" fill="var(--green)"/>
      <polygon points="384,290 562,228 562,262 384,306" fill="var(--green-dark)"/>
    </svg>
    <div class="abs building" role="img" aria-label="Modernes Wohnhochhaus mit begrünten Terrassen"
         style="background:linear-gradient(150deg,#d9d9d6 0%,#c9b48c 35%,#5f8a3c 60%,#3a4a3a 100%);clip-path:polygon(30% 0,100% 10%,100% 78%,48% 100%,20% 70%,0 40%)"></div>

    <div class="abs brand front-brand"><span class="brand__square"></span>werkbaukolleg</div>

    <h1 class="abs headline">Sie Haben Eine<br>Aufgabenstellung...?</h1>
    <p class="abs subline">Gerne sind wir Ihr<br>Lösungspartner...</p>

    <div class="abs intro">
      <svg class="abs" width="314" height="274" aria-hidden="true">
        <polygon points="0,0 282,0 314,30 314,274 14,274 0,260" fill="var(--green)"/>
      </svg>
      <p class="intro__text"><span class="intro__notch"></span><b>werkbaukolleg</b> bieten Ihnen den einmaligen Vorteil von fest eingespielten, hoch qualifizierten und motivierten Handwerker-Teams unter einer gemeinsamen Leitung. So werden Sie von der Beratung über die Projektplanung bis zur Fertigstellung Ihrer Renovierung von nur einem Ansprechpartner betreut und haben dennoch für jedes Gewerk und für jede Aufgabenstellung den passgenauen Handwerksprofi! Wir koordinieren für Sie die zeitliche und fachliche Ausführung der Bauabschnitte in Absprache mit den einzelnen Fachhandwerkern – so ist ein reibungsloser Ablauf und eine termingerechte Fertigstellung aller Arbeiten gewährleistet. Sparen Sie sich das Risiko von zusammengewürfelten Handwerkerfirmen - arbeiten Sie einfach mit nur einem qualifizierten Partner für alle Gewerke zusammen. Denn bei werkbaukolleg passt alles zusammen, so dass Sie sich in Ihrem Zuhause wirklich wohl fühlen können.</p>
    </div>

    <div class="abs comp-title">
      <div class="comp-title__light">UNSERE</div>
      <div class="comp-title__bold">KOMPETENZEN</div>
    </div>

    <div class="tile tile--outline" style="left:341px;top:369px"><i class="tile__icon"></i><span>Umfassende<br>Baubetreuung</span></div>
    <div class="tile tile--dark" style="left:412px;top:369px"><i class="tile__icon"></i><span>Deutschlandweit<br>Tätig</span></div>
    <div class="tile tile--soft" style="left:482px;top:369px"><i class="tile__icon"></i><span>Langjährige<br>Erfahrung</span></div>
    <div class="tile tile--mid" style="left:341px;top:465px"><i class="tile__icon"></i><span>Mitarbeiter Aus Allen<br>Handwerksbereichen</span></div>
    <div class="tile tile--soft" style="left:412px;top:465px"><i class="tile__icon"></i><span>Umfangreiches<br>Partnernetzwerk</span></div>
    <div class="tile tile--mid" style="left:482px;top:465px"><i class="tile__icon"></i><span>Alle Leistungen<br>Aus Einer Hand</span></div>
  </section>

  <section class="panel panel--back">
    <svg class="abs" style="left:0;top:0" width="562" height="562" aria-hidden="true">
      <polygon points="0,0 381,0 249,84 0,84" fill="var(--green)"/>
      <polyline points="33,384 522,384 546,408 546,471" fill="none" stroke="var(--green-dark)" stroke-width="1.3"/>
    </svg>
    <div class="abs services-head">
      <div class="services-head__light">AUSZUG AUS</div>
      <div class="services-head__bold">UNSEREN LEISTUNGEN</div>
    </div>

    <ul class="abs services services--left">
      <li>Abbrucharbeiten</li><li>Blechnerarbeiten</li><li>Bodenbelagsarbeiten</li><li>Dachdeckerarbeiten</li><li>Elektroarbeiten</li><li>Fassadenarbeiten</li><li>Fliesenarbeiten</li><li>Gartenarbeiten</li><li>Heizungsarbeiten</li>
    </ul>
    <ul class="abs services services--right">
      <li>Komplettsanierungen</li><li>Lackierarbeiten</li><li>Malerarbeiten</li><li>Reinigungsarbeiten</li><li>Rohbauarbeiten</li><li>Sanitärarbeiten</li><li>Schlosserarbeiten</li><li>Schreinerarbeiten</li><li>Trockenbauarbeiten</li>
    </ul>

    <p class="abs claim">Vom Anstrich bis zur Komplettsanierung-Wir sind für <b>SIE</b> da!</p>

    <div class="abs brand back-brand"><span class="brand__square"></span>werkbaukolleg</div>

    <div class="abs contact" style="left:264px;top:428px">
      <div class="contact__row" style="top:0">
        <svg width="20" height="20" viewBox="0 0 24 24"><circle cx="12" cy="12" r="10.5" fill="none" stroke="var(--green-dark)" stroke-width="2"/><path d="M8.5 6.5c-.8.4-1.6 1.5-1 3 1 2.7 3.5 5.4 6.3 6.7 1.5.6 2.6-.2 3-1l-2-1.8-1.4.8c-1.4-.7-2.6-2-3.3-3.4l.8-1.4z" fill="var(--green-dark)"/></svg>
        <span class="contact__phone">06221-4471300</span>
      </div>
      <div class="contact__row" style="top:33px">
        <svg width="16" height="16" viewBox="0 0 24 24"><path d="M12 2a7 7 0 0 0-7 7c0 5 7 13 7 13s7-8 7-13a7 7 0 0 0-7-7z" fill="none" stroke="var(--green-dark)" stroke-width="2"/><circle cx="12" cy="9" r="2.5" fill="none" stroke="var(--green-dark)" stroke-width="2"/></svg>
        <span>Am Lindenhang 12<br>69190 Walldorf</span>
      </div>
      <div class="contact__row" style="top:74px">
        <svg width="16" height="16" viewBox="0 0 24 24"><rect x="3" y="6" width="18" height="12" rx="1" fill="none" stroke="var(--green-dark)" stroke-width="2"/><path d="M3 7l9 6 9-6" fill="none" stroke="var(--green-dark)" stroke-width="2"/></svg>
        <span>kontakt@werkbaukolleg.de</span>
      </div>
      <div class="contact__row" style="top:96px">
        <svg width="16" height="16" viewBox="0 0 24 24"><circle cx="12" cy="12" r="9" fill="none" stroke="var(--green-dark)" stroke-width="2"/><path d="M3 12h18M12 3c3 3 3 15 0 18M12 3c-3 3-3 15 0 18" fill="none" stroke="var(--green-dark)" stroke-width="1.6"/></svg>
        <span>www.werkbaukolleg.de</span>
      </div>
    </div>
  </section>

</div>
</body>
</html>
```